Produktetikett für Mikronährstoffe
Wir sind sehr zufrieden und schätzen die schnelle Umsetzung von Änderungswünschen. Herzlichen Dank an Wilmaru
Zielgruppe
Herstellung und Vertrieb von Desinfektionsmitteln und jetz neu Mikronährstoffe. Und darum geht es. Wir möchten ein Etikett gestalten lassen das modern ist und trotzdem unsere Firmenfarben und unser Logo (evtl. stilisiert) enthält. Wahrscheinlich werden wir eine braune Flasche (ähnl. Apothekerflaschen) wählen.
Aufgabenstellung
Produktetikett für Mikronährstoffe (im Nahrungsergänzungsbereich) Die Ausführung der Flasche ist noch nicht bekannnt, jedoch schwebt uns eine braune oder dunkelgrüne Flasche vor. Auch gibt es noch keinen Namen für das Produkt.

```html
<!DOCTYPE html>
<html lang="de">
<head>
<meta charset="utf-8">
<title>Mikronährstoffe – Produktetiketten</title>
<link rel="stylesheet" href="https://fonts.googleapis.com/css2?family=Jost:wght@400;500;600&display=swap">
<style>
  :root {
    --page-bg: #f4f4f4;
    --label-blue: #3f9dc0;
    --label-blue-dark: #33829f;
    --label-green: #a2bd37;
    --label-green-dark: #86a02c;
    --cream: #f6ebdc;
    --dot-green: #c4d06a;
    --dot-blue: #6fb8cb;
    --ink: #1e1b1a;
    --brand: #9dba35;
    --caption: #f3efe6;
  }
  html, body {
    margin: 0;
    padding: 0;
    width: 1200px;
    height: 1138px;
    overflow: hidden;
    background: var(--page-bg);
  }
  .canvas {
    position: relative;
    width: 1200px;
    height: 1138px;
  }
  .product-label {
    position: absolute;
    top: 482px;
    width: 238px;
    height: 237px;
  }
  .product-label--blue { left: 273px; }
  .product-label--green { left: 673px; }
  .product-label svg { display: block; width: 100%; height: 100%; }
  .brand-name {
    font-family: "Jost", sans-serif;
    font-weight: 600;
    font-size: 15px;
    fill: var(--brand);
    letter-spacing: -0.3px;
  }
  .title-light {
    font-family: "Jost", sans-serif;
    font-weight: 400;
    font-size: 29px;
    letter-spacing: 2.5px;
    fill: var(--ink);
  }
  .title-bold {
    font-family: "Jost", sans-serif;
    font-weight: 600;
    font-size: 30px;
    letter-spacing: 3px;
    fill: var(--ink);
  }
  .caption {
    font-family: "Jost", sans-serif;
    font-weight: 400;
    font-size: 14px;
    fill: var(--caption);
  }
</style>
</head>
<body>
<main class="canvas">

  <section class="product-label product-label--blue" aria-label="Etikett Mikronährstoffe, blau">
    <svg viewBox="0 0 354 352" xmlns="http://www.w3.org/2000/svg">
      <defs>
        <linearGradient id="blue-sheen" x1="0" x2="1" y1="0" y2="0">
          <stop offset="0" stop-color="var(--label-blue-dark)"/>
          <stop offset="0.12" stop-color="var(--label-blue)"/>
          <stop offset="0.5" stop-color="var(--label-blue-dark)"/>
          <stop offset="0.88" stop-color="var(--label-blue)"/>
          <stop offset="1" stop-color="var(--label-blue-dark)"/>
        </linearGradient>
      </defs>
      <rect class="label-base" width="354" height="352" rx="12" fill="url(#blue-sheen)"/>
      <circle class="emblem-disc" cx="178" cy="167" r="131" fill="var(--cream)"/>
      <circle class="accent-dot" cx="146" cy="196" r="70" fill="var(--dot-green)"/>
      <circle class="brand-mark" cx="211" cy="76" r="5" fill="var(--brand)"/>
      <text class="brand-name" x="170" y="69" text-anchor="middle">KALVIMO</text>
      <text class="title-light" x="178" y="150" text-anchor="middle">MIKRO</text>
      <text class="title-bold" x="178" y="183" text-anchor="middle">NÄHRSTOFFE</text>
      <text class="caption" x="177" y="329" text-anchor="middle">Lorem ipsum dolor sit amet, consectetuer</text>
    </svg>
  </section>

  <section class="product-label product-label--green" aria-label="Etikett Mikronährstoffe, grün">
    <svg viewBox="0 0 354 352" xmlns="http://www.w3.org/2000/svg">
      <defs>
        <linearGradient id="green-sheen" x1="0" x2="1" y1="0" y2="0">
          <stop offset="0" stop-color="var(--label-green-dark)"/>
          <stop offset="0.12" stop-color="var(--label-green)"/>
          <stop offset="0.5" stop-color="var(--label-green-dark)"/>
          <stop offset="0.88" stop-color="var(--label-green)"/>
          <stop offset="1" stop-color="var(--label-green-dark)"/>
        </linearGradient>
      </defs>
      <rect class="label-base" width="354" height="352" rx="12" fill="url(#green-sheen)"/>
      <circle class="emblem-disc" cx="178" cy="167" r="131" fill="var(--cream)"/>
      <circle class="accent-dot" cx="146" cy="196" r="70" fill="var(--dot-blue)"/>
      <circle class="brand-mark" cx="211" cy="76" r="5" fill="var(--brand)"/>
      <text class="brand-name" x="170" y="69" text-anchor="middle">KALVIMO</text>
      <text class="title-light" x="178" y="150" text-anchor="middle">MIKRO</text>
      <text class="title-bold" x="178" y="183" text-anchor="middle">NÄHRSTOFFE</text>
      <text class="caption" x="177" y="329" text-anchor="middle">Lorem ipsum dolor sit amet, consectetuer</text>
    </svg>
  </section>

</main>
</body>
</html>
```